Modern and Clean Photograper´s Business Card

It´s a Personal Photographer´s business card that communicates elegance, modernity, efficiency.

Target Market(s)

people that wants an efficient and qualified photographer

Industry/Entity Type

Business

Contact Information for Business Card

modern, elegant, clean

Logo Text

TalvenKo fotografia

Font styles to use
Serif
Sans Serif
Script

Colors

Designer to choose colors to be used in the design.

Requirements
Must have
• one symbol per design.
• colors that match
Nice to have
• photography simbols like shutter, camera,movement.
• blended symbols like this designs: 15160747 and 5900864
Should not have
• logo symbol too big
• colors that don´t match
• loaded of symbols, and looks like bloated.

```html
<!DOCTYPE html>
<html lang="en">
<head>
<meta charset="utf-8">
<title>TalvenKo fotografia — Business Card</title>
<link rel="stylesheet" href="https://fonts.googleapis.com/css2?family=Roboto:wght@400;700;900&display=swap">
<style>
  :root {
    --stage: #3a3a3c;
    --card-dark: #03040c;
    --card-light: #ffffff;
    --ink: #1d2124;
    --ink-soft: #2b2f33;
    --white: #ffffff;
    --mark-dark: #9a9ca0;
    --mark-light: #2a2c30;
  }
  * { margin: 0; padding: 0; box-sizing: border-box; }
  html, body {
    width: 1200px; height: 810px; overflow: hidden;
    background: var(--stage);
    font-family: "Roboto", Arial, sans-serif;
  }
  .stage { position: relative; width: 1200px; height: 810px; }
  .card {
    position: absolute; left: 300px; width: 600px; height: 343px;
    box-shadow: 0 8px 24px rgba(0,0,0,.35);
  }
  .card--front { top: 40px; background: var(--card-dark); color: var(--white); }
  .card--back { top: 427px; background: var(--card-light); color: var(--ink); }

  .brand-mark { position: absolute; border-radius: 50%; }
  .card--front .brand-mark {
    left: 130px; top: 131px; width: 82px; height: 82px;
    background: var(--mark-dark);
  }
  .card--back .brand-mark {
    left: 78px; top: 92px; width: 94px; height: 94px;
    background: var(--mark-light);
  }

  .brand-name { position: absolute; font-weight: 700; line-height: 1; }
  .brand-name .name { display: block; letter-spacing: .5px; }
  .brand-name .role { display: block; text-align: right; font-weight: 700; }
  .card--front .brand-name { left: 232px; top: 132px; }
  .card--front .brand-name .name { font-size: 44px; }
  .card--front .brand-name .role { font-size: 21px; margin-top: 4px; }
  .card--back .brand-name { left: 228px; top: 52px; color: var(--ink); }
  .card--back .brand-name .name { font-size: 54px; }
  .card--back .brand-name .role { font-size: 26px; margin-top: 4px; }

  .contacts { position: absolute; left: 70px; top: 222px; list-style: none; }
  .contacts li {
    display: flex; align-items: center; gap: 10px;
    font-size: 16px; color: var(--ink-soft); height: 24px;
  }
  .icon {
    width: 18px; height: 18px; background: var(--ink);
    display: inline-flex; align-items: center; justify-content: center; flex: none;
  }
  .address {
    position: absolute; left: 370px; top: 210px;
    display: flex; gap: 10px; font-size: 16px; color: var(--ink-soft); line-height: 1.3;
  }
  .address .icon { margin-top: 2px; }
</style>
</head>
<body>
<main class="stage">
  <section class="card card--front" aria-label="Card front">
    <span class="brand-mark" aria-hidden="true"></span>
    <h1 class="brand-name"><span class="name">TalvenKo</span><span class="role">Photographer</span></h1>
  </section>

  <section class="card card--back" aria-label="Card back">
    <span class="brand-mark" aria-hidden="true"></span>
    <h2 class="brand-name"><span class="name">TalvenKo</span><span class="role">Photographer</span></h2>

    <ul class="contacts">
      <li><span class="icon"><svg width="12" height="12" viewBox="0 0 12 12"><path d="M2.5 1l2 2.5-1 1.2c.7 1.4 1.6 2.3 3 3l1.2-1 2.3 2-1 1.8C5 10.5 1.5 7 .8 2.3z" fill="#fff"/></svg></span>+971550004821</li>
      <li><span class="icon"><svg width="12" height="10" viewBox="0 0 12 10"><rect x=".5" y=".5" width="11" height="9" fill="none" stroke="#fff"/><path d="M.5 .5l5.5 5 5.5-5" fill="none" stroke="#fff"/></svg></span>info@yourwebsite.com</li>
      <li><span class="icon"><svg width="8" height="8" viewBox="0 0 8 8"><rect width="8" height="8" fill="#fff"/></svg></span>social/yourwebsite.com</li>
      <li><span class="icon"><svg width="12" height="12" viewBox="0 0 12 12"><circle cx="6" cy="6" r="5" fill="none" stroke="#fff"/><path d="M1 6h10M6 1c-2.5 3-2.5 7 0 10M6 1c2.5 3 2.5 7 0 10" fill="none" stroke="#fff"/></svg></span>www.yourwebsite.com</li>
    </ul>

    <div class="address">
      <span class="icon"><svg width="10" height="13" viewBox="0 0 10 13"><path d="M5 .5a4.5 4.5 0 0 0-4.5 4.5C.5 8 5 12.5 5 12.5S9.5 8 9.5 5A4.5 4.5 0 0 0 5 .5z" fill="#fff"/><circle cx="5" cy="5" r="1.6" fill="#1d2124"/></svg></span>
      <p>18 Lindell Ave.<br>North Ashford, CT 06090</p>
    </div>
  </section>
</main>
</body>
</html>
```